General contractor/GM consaltant business card

I need a card for my contracting company in North Dakota, we build industrial buildings for the oil feild and oil feild related companies offices, shops, airplain hangars, airports ext. We have a familly atmosphere on the job and are very relational and personal.
Industry/Entity Type
Industrial
Contact Information for Business Card
Hollowpine Crafters LLC.
Dale T.Voskuijl
4873 Quenwick dr. Colorado Springs, CO. 80462
Cell# 406-738-1452
dale@hollowpinecrafters.example

```html
<!DOCTYPE html>
<html lang="en">
<head>
<meta charset="utf-8">
<title>Hollowpine Crafters LLC. – Business Card</title>
<link rel="stylesheet" href="https://fonts.googleapis.com/css2?family=Alegreya+Sans:wght@700&family=Alegreya:wght@400;700&display=swap">
<style>
  :root {
    --page-bg: #e6e6e6;
    --ink-dark: #141414;
    --ink-light: #f4f4f4;
    --ink-muted: #e2e2e2;
    --card-dark: #3b3b3b;
    --card-dark-edge: #2e2e2e;
    --mark-grey: #8a8a8a;
    --photo-top: #d8cbb0;
    --photo-mid: #e3a85a;
    --photo-bottom: #3a2a1a;
  }
  * { margin: 0; padding: 0; box-sizing: border-box; }
  html, body {
    width: 1200px;
    height: 900px;
    overflow: hidden;
    background: var(--page-bg);
  }
  .canvas {
    width: 1200px;
    height: 900px;
    display: flex;
    flex-direction: column;
    align-items: center;
    justify-content: center;
    gap: 56px;
  }
  .card {
    position: relative;
    width: 620px;
    height: 354px;
    border-radius: 12px;
    overflow: hidden;
  }

  /* Front */
  .card--front .photo {
    position: absolute;
    inset: 0;
    background: linear-gradient(to bottom, var(--photo-top) 0%, var(--photo-mid) 55%, var(--photo-bottom) 100%);
  }
  .brand {
    position: absolute;
    display: flex;
    align-items: center;
    gap: 22px;
  }
  .card--front .brand { left: 48px; top: 62px; }
  .brand__square {
    width: 64px;
    height: 64px;
    flex: none;
  }
  .card--front .brand__square { background: var(--ink-dark); }
  .brand__name {
    font-family: "Alegreya Sans", sans-serif;
    font-weight: 700;
    font-size: 70px;
    line-height: 0.9;
    letter-spacing: 0.2px;
  }
  .card--front .brand__name { color: var(--ink-dark); }

  /* Back */
  .card--back {
    background: linear-gradient(135deg, var(--card-dark) 0%, var(--card-dark-edge) 100%);
  }
  .card--back .brand { left: 40px; top: 34px; }
  .card--back .brand__square { background: var(--mark-grey); }
  .card--back .brand__name { color: var(--ink-light); }
  .contact {
    position: absolute;
    left: 40px;
    top: 190px;
    font-family: "Alegreya", serif;
    font-style: normal;
    color: var(--ink-muted);
    font-size: 18px;
    line-height: 1.3;
  }
  .contact__name {
    font-weight: 700;
    font-size: 23px;
    color: var(--ink-light);
    margin-bottom: 4px;
  }
</style>
</head>
<body>
<main class="canvas">
  <section class="card card--front">
    <div class="photo" role="img" aria-label="Photograph of an oil field with pump jacks and power poles at sunset"></div>
    <div class="brand">
      <span class="brand__square"></span>
      <h1 class="brand__name">Hollowpine<br>Crafters LLC.</h1>
    </div>
  </section>

  <section class="card card--back">
    <div class="brand">
      <span class="brand__square"></span>
      <h2 class="brand__name">Hollowpine<br>Crafters LLC.</h2>
    </div>
    <address class="contact">
      <p class="contact__name">Dale T.Voskuijl</p>
      <p>4873 Quenwick dr.</p>
      <p>Colorado Springs, CO. 80462</p>
      <p>Cell# 406-738-1452</p>
      <p>dale@hollowpinecrafters.example</p>
    </address>
  </section>
</main>
</body>
</html>
```